Premium Skincare Packaging Design for Vale Hollow

Vale Hollow (https://valehollowgoods.com) is a premium wellness brand from Canada specializing in beef tallow (for cooking) and now expanding into natural skincare. We are seeking packaging design concepts for two new 60 ml skincare products made with grass-fed beef tallow.
Our goal is to achieve a clean, minimalist yet luxurious look that reflects purity, quality and sophistication. The design should look premium enough for high-end skincare shelves while maintaining a natural, grounded feel.
You will be designing:
- Jar label (wrap-around design) for a 60 ml glass jar with black lid
- Round lid sticker (for the top of the black lid)
- Square outer box (for each jar)
- Both products are very similar, so the differentiation can be minimal.

Products to Design
1. Everyday Suet Salve
Jar: Frosted glass, 60 ml with black lid
Purpose: Moisturizer for face, lips, hands, and body
Ingredients: Grass-fed beef tallow, beeswax, honey, vitamin E
Tone: Natural, pure, versatile, gentle
Tagline: “Crafted from nature’s simplest elements”
Preferred color palette:
Light / off-white background
Beige and honey accents
Black or dark brown typography
Mood: Minimalist apothecary meets warm, natural simplicity
2. Visage Suet Lotion
Purpose: Face moisturizer with nourishing tallow and botanicals
Tone: Refined, elegant, modern, premium
Tagline: “The strength of tallow, refined for your face”
Preferred color palette:
Deep charcoal or black background
Gold or cream typography
Accent in subtle metallic tones (gold or bronze)
Mood: Modern luxury with understated confidence
Design Deliverables
For each product, submit:
1) Jar Label (Wrap-around)
- Include product name, logo, tagline, ingredients, and size (60 ml / 2 fl oz).
- Space for barcode and manufacturing details (leave placeholder).
2) Round Lid Sticker
- Centered logo and minimalist border or accent ring.
3) Outer Paper Box (Square)
- Matching color palette and typography.
- Clean layout featuring the Vale Hollow logo and tagline.
- Text to include: product name, tagline, ingredients and size.

Brand Guidelines
Logo: Use the existing Vale Hollow logo (we’ll upload it for reference).
Typography: Clean and elegant — sans-serif or classic serif fonts.
Tone: Pure, premium, and intentional — less is more.
Design cohesion: Both products must look like part of one collection.

```html
<!DOCTYPE html>
<html lang="en">
<head>
<meta charset="utf-8">
<title>Vale Hollow — Everyday Suet Salve Packaging</title>
<link rel="stylesheet" href="https://fonts.googleapis.com/css2?family=Archivo:wght@400;500;600&display=swap">
<style>
  :root {
    --canvas: #f6f6f6;
    --paper: #f0d5ab;
    --paper-deep: #e2c69c;
    --ink: #2f2b27;
    --band: #2b2926;
    --band-text: #efe2cc;
    --lid: #2c2c2c;
    --lid-edge: #1b1b1b;
    --gold: #d8bd95;
  }
  * { box-sizing: border-box; margin: 0; padding: 0; }
  html, body { width: 1200px; height: 750px; overflow: hidden; }
  body {
    background: var(--canvas);
    font-family: "Archivo", Arial, sans-serif;
    color: var(--ink);
    position: relative;
  }
  .panel {
    position: absolute;
    background: linear-gradient(135deg, var(--paper) 0%, var(--paper-deep) 100%);
  }

  .brand {
    position: absolute; display: flex; align-items: center; gap: 8px;
    font-weight: 500; text-transform: uppercase; letter-spacing: .14em; color: var(--ink);
    white-space: nowrap;
  }
  .brand-mark { width: 14px; height: 14px; background: var(--ink); }

  /* Box top panel */
  .box-top { left: 370px; top: 20px; width: 340px; height: 340px; }
  .box-top .brand { left: 0; right: 0; top: 0; bottom: 0; justify-content: center; font-size: 20px; }

  /* Box side panel */
  .box-side { left: 20px; top: 370px; width: 340px; height: 340px; }
  .maker {
    position: absolute; left: 24px; bottom: 36px;
    font-size: 9px; line-height: 1.3; text-transform: uppercase; letter-spacing: .02em;
  }

  /* Box front panel */
  .box-front { left: 370px; top: 370px; width: 340px; height: 340px; }
  .box-front .brand { right: 24px; top: 34px; font-size: 18px; }

  .title {
    position: absolute; font-weight: 600; text-transform: uppercase;
    line-height: .95; letter-spacing: .01em;
  }
  .box-front .title { left: 24px; top: 138px; font-size: 36px; }

  .band {
    position: absolute; background: var(--band); color: var(--band-text);
    font-weight: 600; text-transform: uppercase; white-space: nowrap;
    display: flex; align-items: center; padding-left: 8px;
  }
  .box-front .band { left: 24px; right: 24px; top: 252px; height: 17px; font-size: 7.5px; }

  .tagline { position: absolute; font-size: 11.5px; white-space: nowrap; }
  .box-front .tagline { left: 24px; top: 277px; }
  .rule { position: absolute; height: 1.5px; background: var(--ink); }
  .box-front .rule { left: 24px; width: 210px; top: 295px; }
  .ingredients { position: absolute; font-size: 11.5px; line-height: 1.2; }
  .box-front .ingredients { left: 24px; top: 302px; }

  .size {
    position: absolute; font-size: 8.5px; writing-mode: vertical-rl; transform: rotate(180deg);
  }
  .box-front .size { right: 26px; top: 178px; }

  /* Lid sticker */
  .lid {
    position: absolute; left: 835px; top: 40px; width: 260px; height: 260px; border-radius: 50%;
    background: radial-gradient(circle at 40% 35%, var(--lid) 0%, var(--lid-edge) 100%);
  }
  .lid .brand { left: 0; right: 0; top: 0; bottom: 0; justify-content: center; color: var(--gold); font-size: 18px; }
  .lid .brand-mark { background: var(--gold); }

  /* Jar wrap label */
  .jar-label { left: 760px; top: 330px; width: 410px; height: 270px; }
  .jar-label .brand { right: 24px; top: 24px; font-size: 17px; }
  .jar-label .title { left: 22px; top: 62px; font-size: 36px; }
  .jar-label .band { left: 22px; right: 24px; top: 176px; height: 16px; font-size: 8.5px; }
  .jar-label .tagline { left: 22px; top: 199px; font-size: 11px; }
  .jar-label .rule { left: 22px; width: 220px; top: 216px; }
  .jar-label .ingredients { left: 22px; top: 223px; font-size: 10.5px; }
  .jar-label .size { right: 26px; top: 110px; font-size: 8px; }
</style>
</head>
<body>
  <section class="panel box-top" aria-label="Outer box, top panel">
    <div class="brand"><span class="brand-mark"></span>Vale Hollow</div>
  </section>

  <section class="panel box-side" aria-label="Outer box, side panel">
    <p class="maker">Manufactured by:<br>Vale Hollow, LLC<br>36 Cedar Row,<br>Nelson, BC</p>
  </section>

  <section class="panel box-front" aria-label="Outer box, front panel">
    <div class="brand"><span class="brand-mark"></span>Vale Hollow</div>
    <h1 class="title">Everyday<br>Suet<br>Salve</h1>
    <div class="band">Face moisturizer with nourishing tallow and botanicals</div>
    <p class="tagline">The strength of tallow, refined for your face</p>
    <div class="rule"></div>
    <p class="ingredients">Ingredients: Grass-fed beef tallow,<br>beeswax, honey, vitamin E</p>
    <span class="size">60ml 2oz</span>
  </section>

  <section class="lid" aria-label="Round lid sticker">
    <div class="brand"><span class="brand-mark"></span>Vale Hollow</div>
  </section>

  <section class="panel jar-label" aria-label="Jar wrap label">
    <div class="brand"><span class="brand-mark"></span>Vale Hollow</div>
    <h2 class="title">Everyday<br>Suet<br>Salve</h2>
    <div class="band">Moisturizer for face, lips, hands, and body</div>
    <p class="tagline">Crafted from nature’s simplest elements</p>
    <div class="rule"></div>
    <p class="ingredients">Ingredients: Grass-fed beef tallow,<br>beeswax, honey, vitamin E</p>
    <span class="size">60ml 2oz</span>
  </section>
</body>
</html>
```